" uma empresa que atua no desenvolvimento de soluçoes corporativas em Tecnologia da Informaçao. Com atendimento personalizado, detecta as necessidades de cada cliente e busca aplicar a melhor soluçao tecnológica para cada caso, agregando valor e fazendo um diferencial significativo. Procura integrar soluçoes que traduzam de forma verdadeira a melhor relaçao investimentos/resultados. Qualidade no atendimento, soluçoes otimizadas, segurança e inovaçao tecnológica em prol do cliente. "

```html
<!DOCTYPE html>
<html lang="pt-BR">
<head>
<meta charset="UTF-8">
<title>Kordel – Cartão de visita</title>
<link rel="stylesheet" href="https://fonts.googleapis.com/css2?family=Open+Sans:wght@400;600;700;800&display=swap">
<style>
  :root {
    --page-bg: #e9ecef;
    --card-white: #ffffff;
    --brand-blue: #1f6fa8;
    --brand-blue-light: #3a93cf;
    --brand-blue-deep: #165582;
    --strip-navy: #1d2f47;
    --text-white: #ffffff;
    --text-soft: #d6e9f6;
    --swoosh: #b9d8ee;
  }
  * { box-sizing: border-box; margin: 0; padding: 0; }
  html, body { width: 1200px; height: 1200px; overflow: hidden; }
  body {
    background: var(--page-bg);
    font-family: "Open Sans", Arial, sans-serif;
    position: relative;
  }
  .card {
    position: absolute;
    left: 160px;
    width: 880px;
    height: 503px;
    border-radius: 28px;
    overflow: hidden;
    box-shadow: 0 10px 30px rgba(20, 40, 60, 0.18);
  }

  /* Front */
  .card-front { top: 70px; background: var(--card-white); }
  .card-front .swoosh { position: absolute; inset: 0; }
  .front-logo {
    position: absolute;
    left: 0; right: 0; top: 150px;
    text-align: center;
  }
  .brand-name {
    display: inline-flex;
    align-items: center;
    gap: 18px;
    font-weight: 800;
    font-size: 104px;
    letter-spacing: 2px;
    color: var(--brand-blue);
    line-height: 1;
  }
  .brand-dot {
    width: 34px; height: 34px;
    border-radius: 50%;
    background: var(--brand-blue-light);
  }
  .brand-tagline {
    margin-top: 14px;
    font-size: 19px;
    font-weight: 600;
    letter-spacing: 5px;
    color: var(--brand-blue);
  }

  /* Back */
  .card-back {
    top: 627px;
    background: linear-gradient(135deg, var(--brand-blue-light) 0%, var(--brand-blue) 50%, var(--brand-blue-deep) 100%);
    color: var(--text-white);
  }
  .back-illustration {
    position: absolute;
    left: 250px; top: 70px;
    width: 230px; height: 400px;
    border-radius: 20px;
    background: radial-gradient(ellipse at center, rgba(15, 50, 80, 0.35), rgba(15, 50, 80, 0));
  }
  .social-strip {
    position: absolute;
    top: 0; right: 0; bottom: 0;
    width: 72px;
    background: var(--strip-navy);
    display: flex;
    flex-direction: column;
    align-items: center;
    justify-content: center;
    gap: 30px;
  }
  .social-strip span {
    width: 22px; height: 22px;
    border-radius: 50%;
    background: #c9d6e2;
  }
  .contact {
    position: absolute;
    right: 110px; top: 46px;
    text-align: right;
  }
  .person-name { font-size: 46px; font-weight: 400; line-height: 1.1; }
  .person-role { font-size: 15px; font-weight: 600; color: var(--text-soft); margin-bottom: 22px; }
  .contact-line { font-size: 20px; line-height: 1.4; color: var(--text-soft); }
  .contact-line strong { color: var(--text-white); font-weight: 700; }
  .address { margin-top: 44px; }
  .phone { font-size: 26px; color: var(--text-white); line-height: 1.3; }
  .phone strong { font-weight: 700; }
  .back-logo {
    position: absolute;
    left: 60px; bottom: 60px;
    display: flex; align-items: center; gap: 10px;
    font-size: 48px; font-weight: 800; letter-spacing: 1px;
    color: var(--text-white);
  }
  .back-logo .brand-dot { width: 16px; height: 16px; background: var(--text-white); }
</style>
</head>
<body>
  <section class="card card-front" aria-label="Frente do cartão">
    <svg class="swoosh" viewBox="0 0 880 503" preserveAspectRatio="none" aria-hidden="true">
      <defs>
        <linearGradient id="swooshFill" x1="0" y1="0" x2="0" y2="1">
          <stop offset="0" stop-color="#ffffff" stop-opacity="0"/>
          <stop offset="1" stop-color="#8fc0e4"/>
        </linearGradient>
      </defs>
      <path d="M0 380 C 250 470, 560 300, 880 330 L 880 503 L 0 503 Z" fill="url(#swooshFill)"/>
      <path d="M0 430 C 300 500, 600 360, 880 400 L 880 503 L 0 503 Z" fill="#4a9ad3" opacity="0.55"/>
    </svg>
    <div class="front-logo">
      <div class="brand-name">KORDEL<span class="brand-dot"></span></div>
      <div class="brand-tagline">SOLUÇÕES EM INFORMÁTICA</div>
    </div>
  </section>

  <section class="card card-back" aria-label="Verso do cartão">
    <div class="back-illustration" role="img" aria-label="Ilustração suave de pessoa trabalhando ao computador"></div>
    <div class="contact">
      <div class="person-name">Rafael Montanari</div>
      <div class="person-role">diretor comercial</div>
      <div class="contact-line">contato@<strong>kordel</strong>.com.br</div>
      <div class="contact-line">facebook.com/<strong>kordel</strong></div>
      <div class="contact-line">@<strong>kordel</strong></div>
      <div class="address">
        <div class="contact-line">Endereço Completo, 00 &nbsp;Bairro</div>
        <div class="contact-line">CEP 00000-000 &nbsp;Cidade SP</div>
        <div class="phone">T.: (00)<strong>0000.0000</strong></div>
        <div class="contact-line">www.<strong>kordel</strong>.com.br</div>
      </div>
    </div>
    <div class="back-logo">KORDEL<span class="brand-dot"></span></div>
    <div class="social-strip" aria-hidden="true">
      <span></span><span></span><span></span><span></span><span></span><span></span>
    </div>
  </section>
</body>
</html>
```